[Bright Oak Mixer] Make a flyer for a networking event/product soft launch

*****We are looking for a graphic designer to create a flyer that is exciting, and fits for a professional audience.*****

Why? We are hosting an end of the year event for our community to get together, network, and celebrate the end of the year. In addition, we're going to share a short presentation to highlight our website and Job Board.

Please see below for what the flyer must include:

(1.) Company logo (attached black or white)
(2.) Event Title: "Bright Oak Mixer"
(3.) Sub text: "Come network with others we share the functionality of the Bright Oak Job board and company updates. This event is limited to 40 people. First come first served. Must register to attend."
(4.) Time: "6-7:30pm"
(5.) Date: "Dec. 16th"
(6.) Venue: "Tellvane Showcase Hall"
(7.) Text: "Registration Required: brightoak.example/events"
(8.) Must Include Bright Oak Black & Gold (may also include any colors listed below)
(9.) Format Size: 1080x1080
(10.) Send us the photoshop design file

Colors:
Bright Oak Gold: #c79500
Bright Oak Black: #000000
Maroon: #440001
Light Blue: #1a75cf
Green: #6eba75
Purple: #663399

```html
<!DOCTYPE html>
<html lang="en">
<head>
<meta charset="utf-8">
<title>Bright Oak Mixer</title>
<link rel="stylesheet" href="https://fonts.googleapis.com/css2?family=Poppins:wght@400;500;600&display=swap">
<style>
  :root {
    --backdrop: #fdf3f3;
    --black: #000000;
    --white: #ffffff;
    --gold: #c79500;
    --gold-light: #e0bb45;
    --gold-deep: #a87c08;
    --photo-dark: #2e2513;
    --photo-mid: #7d6228;
    --photo-light: #c9a75a;
  }
  * { margin: 0; padding: 0; box-sizing: border-box; }
  html, body {
    width: 1200px; height: 1183px; overflow: hidden;
    background: var(--backdrop);
    font-family: "Poppins", sans-serif;
  }
  .flyer {
    position: absolute; left: 168px; top: 159px;
    width: 865px; height: 865px; overflow: hidden;
    background: var(--white);
  }
  .header {
    position: absolute; left: 0; top: 0; width: 865px; height: 178px;
    background: var(--black);
    display: flex; align-items: center; justify-content: center; gap: 22px;
    color: var(--white);
  }
  .brand-name { font-size: 58px; font-weight: 500; letter-spacing: 1px; }
  .event-word { font-size: 94px; font-weight: 500; letter-spacing: 1px; }
  .photo {
    position: absolute; left: 0; top: 178px; width: 865px; height: 503px;
    background:
      linear-gradient(180deg, rgba(190,150,60,0.55) 0%, rgba(60,45,20,0.25) 60%, rgba(30,24,12,0.6) 100%),
      radial-gradient(ellipse at 60% 55%, var(--photo-light) 0%, var(--photo-mid) 45%, var(--photo-dark) 100%);
  }
  .intro-box {
    position: absolute; left: 57px; top: 202px; width: 752px; height: 97px;
    border: 2px solid var(--white);
    display: flex; align-items: center; justify-content: center;
    text-align: center; color: var(--white);
    font-size: 19.5px; line-height: 1.3; padding: 0 14px;
  }
  .shapes { position: absolute; left: 0; top: 0; }
  .date-icon { position: absolute; left: 590px; top: 570px; width: 72px; height: 72px; }
  .date-text {
    position: absolute; left: 683px; top: 566px;
    font-size: 28px; font-weight: 500; line-height: 1.35; color: var(--black);
  }
  .location-pill {
    position: absolute; left: 28px; top: 745px; height: 33px; padding: 0 10px;
    border-radius: 17px; background: var(--gold-light);
    font-size: 20px; font-weight: 500; line-height: 33px; color: var(--black);
  }
  .venue {
    position: absolute; left: 36px; top: 775px;
    font-size: 20px; font-weight: 500; color: var(--black);
  }
  .registration {
    position: absolute; left: 385px; top: 762px;
    font-size: 19px; font-weight: 500; color: var(--white); white-space: nowrap;
  }
  .registration .url { color: var(--gold-light); margin-left: 6px; }
</style>
</head>
<body>
<main class="flyer">
  <header class="header">
    <span class="brand-name">BRIGHT OAK</span>
    <span class="event-word">MIXER</span>
  </header>

  <div class="photo" role="img" aria-label="Gold-toned photo of professionals mingling and talking at a networking event"></div>

  <p class="intro-box">Come network with others we share the functionality of the Bright Oak Job board and company updates. This event is limited to 40 people. First come first served. Must register to attend.</p>

  <svg class="shapes" width="865" height="865" viewBox="0 0 865 865" aria-hidden="true">
    <defs>
      <linearGradient id="goldBand" x1="0" y1="0" x2="1" y2="0">
        <stop offset="0" stop-color="#b88a0a"/>
        <stop offset="0.5" stop-color="#d8b140"/>
        <stop offset="1" stop-color="#c99d1e"/>
      </linearGradient>
    </defs>
    <polygon class="date-panel-edge" points="453,681 573,508 865,508 865,518 585,518 475,681" fill="url(#goldBand)"/>
    <polygon class="date-panel" points="475,681 585,518 865,518 865,681" fill="#ffffff"/>
    <rect class="gold-band" x="0" y="681" width="865" height="40" fill="url(#goldBand)"/>
    <rect class="info-white" x="0" y="721" width="865" height="109" fill="#ffffff"/>
    <polygon class="info-black" points="389,721 865,721 865,830 319,830" fill="#000000"/>
    <rect class="gold-base" x="0" y="830" width="865" height="35" fill="url(#goldBand)"/>
  </svg>

  <svg class="date-icon" viewBox="0 0 72 72" aria-hidden="true">
    <g fill="none" stroke="#c79500" stroke-width="4">
      <rect x="4" y="10" width="50" height="44" rx="4"/>
      <line x1="4" y1="22" x2="54" y2="22"/>
      <line x1="16" y1="4" x2="16" y2="14"/>
      <line x1="42" y1="4" x2="42" y2="14"/>
    </g>
    <g fill="#c79500">
      <rect x="11" y="28" width="7" height="6"/><rect x="22" y="28" width="7" height="6"/><rect x="33" y="28" width="7" height="6"/>
      <rect x="11" y="39" width="7" height="6"/><rect x="22" y="39" width="7" height="6"/>
    </g>
    <circle cx="52" cy="52" r="16" fill="#ffffff" stroke="#c79500" stroke-width="4"/>
    <polyline points="52,43 52,53 59,57" fill="none" stroke="#c79500" stroke-width="3.5" stroke-linecap="round"/>
  </svg>
  <p class="date-text">Dec. 16th<br>6-7:30pm</p>

  <span class="location-pill">Location:</span>
  <p class="venue">Tellvane Showcase Hall</p>
  <p class="registration">Registration Required:<span class="url">brightoak.example/events</span></p>
</main>
</body>
</html>
```